Clean, Fresh Business Card Design Needed

We need a business card design for a new business we have taken over called "Bonders and Fillers". We got a logo through this website which i have attached. We are wanting something that is vibrant but clean and fresh. Our business mainly sells glue. Maybe a cool design/slogan on the back? Modern, sleek.

Industry/Entity Type

Business

Contact Information for Business Card

Name: Ewan Tressider, Managing Director. Address: 164 Kelmond Road, Tauranga 3117, Phone: 07 462 3947 Mobile: 021 354 921 Fax: 07 462 5086 Email: bondfill.mail@pelorix.co.nz, Web: www.stickwarex.co.nz

Font styles to use
Serif

Requirements
Must have
• All business card details, logo.
Nice to have
• Design, slogan on back of card

```html
<!DOCTYPE html>
<html lang="en">
<head>
<meta charset="utf-8">
<title>Bonders and Fillers – Business Card</title>
<link rel="stylesheet" href="https://fonts.googleapis.com/css2?family=Cinzel:wght@400;600&family=Questrial&display=swap">
<style>
  :root {
    --navy: #27337f;
    --ink: #1c1c1f;
    --grey-text: #3a3a3e;
    --card-light: #ffffff;
    --card-shade: #e4e4e6;
    --base-strip: #1e1e21;
    --backdrop: #d9d9dc;
  }
  * { box-sizing: border-box; margin: 0; padding: 0; }
  html, body {
    width: 1200px; height: 997px; overflow: hidden;
    background: var(--backdrop);
  }
  .card {
    position: absolute; left: 250px; width: 700px; height: 400px;
    background: linear-gradient(160deg, var(--card-light) 40%, var(--card-shade) 100%);
    box-shadow: 0 6px 18px rgba(0,0,0,0.18);
    overflow: hidden;
  }
  .card--back { top: 70px; }
  .card--front { top: 527px; }
  .card__bands { position: absolute; inset: 0; width: 700px; height: 400px; }

  /* Back */
  .brand-block {
    position: absolute; left: 130px; top: 92px;
    display: flex; align-items: center; gap: 22px;
  }
  .brand-square { width: 92px; height: 92px; background: var(--navy); border-radius: 12px; }
  .brand-name {
    font-family: "Cinzel", serif; font-weight: 400; color: var(--grey-text);
    font-size: 46px; line-height: 1; letter-spacing: 1px;
  }
  .brand-name span { display: block; font-size: 32px; letter-spacing: 6px; margin-top: 4px; }
  .slogan {
    position: absolute; left: 244px; top: 208px; width: 330px; text-align: center;
    font-family: "Questrial", sans-serif; font-size: 15px; line-height: 1.35; color: var(--grey-text);
  }
  .web {
    position: absolute; left: 0; right: 0; top: 300px; text-align: center;
    font-family: "Questrial", sans-serif; font-size: 17px; letter-spacing: 5px; color: var(--navy);
  }

  /* Front */
  .holder { position: absolute; left: 90px; top: 60px; }
  .holder__name {
    font-family: "Cinzel", serif; font-weight: 400; color: var(--navy);
    font-size: 26px; letter-spacing: 1px;
  }
  .holder__role {
    font-family: "Questrial", sans-serif; font-size: 13px; letter-spacing: 1px; color: var(--ink);
  }
  .front-brand {
    position: absolute; right: 70px; top: 46px;
    display: flex; flex-direction: column; align-items: center; gap: 14px;
  }
  .front-brand .brand-square { width: 96px; height: 80px; }
  .front-brand .brand-name { color: var(--ink); font-size: 44px; text-align: center; }
  .contact-list {
    position: absolute; left: 92px; top: 212px; list-style: none;
    font-family: "Questrial", sans-serif; font-size: 16px; color: var(--ink);
  }
  .contact-list li { height: 32px; line-height: 32px; }
</style>
</head>
<body>

<section class="card card--back" aria-label="Card back">
  <svg class="card__bands" viewBox="0 0 700 400" aria-hidden="true">
    <path d="M440 400 C470 400 472 374 505 374 L700 374 L700 400 Z" fill="var(--navy)"/>
  </svg>
  <div class="brand-block">
    <div class="brand-square"></div>
    <div class="brand-name">Bonders<span>and Fillers</span></div>
  </div>
  <p class="slogan">Glues, Adhesives &amp; Sealants From<br>Industrial Strength Through To Craft Glues</p>
  <p class="web">www.stickwarex.co.nz</p>
</section>

<section class="card card--front" aria-label="Card front">
  <svg class="card__bands" viewBox="0 0 700 400" aria-hidden="true">
    <rect x="0" y="378" width="700" height="22" fill="var(--base-strip)"/>
    <path d="M470 400 C500 400 500 358 540 358 L700 358 L700 400 Z" fill="var(--navy)"/>
    <path d="M0 200 H46 Q60 200 60 214 V364 Q60 378 46 378 H0 Z" fill="var(--navy)"/>
    <g fill="none" stroke="#fff" stroke-width="1.8" stroke-linecap="round" stroke-linejoin="round">
      <path d="M22 222 q8 -6 16 0 l-2 4 h-3 l-1 -2 h-4 l-1 2 h-3 z M24 227 h12 v6 h-12 z"/>
      <rect x="24" y="252" width="12" height="18" rx="2"/>
      <path d="M24 285 h12 v5 M22 290 h16 v8 h-16 z M25 298 v4 h10 v-4"/>
      <rect x="21" y="318" width="18" height="12" rx="1"/>
      <path d="M21 319 l9 7 l9 -7"/>
      <path d="M30 362 c-6 -7 -7 -10 -7 -13 a7 7 0 0 1 14 0 c0 3 -1 6 -7 13 z"/>
      <circle cx="30" cy="349" r="2.3"/>
    </g>
  </svg>
  <div class="holder">
    <p class="holder__name">Ewan Tressider</p>
    <p class="holder__role">MANAGER</p>
  </div>
  <div class="front-brand">
    <div class="brand-square"></div>
    <div class="brand-name">Bonders<span>and Fillers</span></div>
  </div>
  <ul class="contact-list">
    <li>07 462 3947</li>
    <li>021 354 921</li>
    <li>07 462 5086</li>
    <li>bondfill.mail@pelorix.co.nz</li>
    <li>164 Kelmond Road, Tauranga 3117</li>
  </ul>
</section>

</body>
</html>
```